Super-fantastic-interesting infographic of terribly boring content

-Looking to provide a visually engaging snapshot of the average Canadian investor.
-Help people compare their personal financial situation against the infographic (Average).
-We want viewers to feel engaged and interested in the info presented, not confused and irritated.

Data points to present:

The average Canadian snapshot:
* Average Canadian household Income in 2016: $76,900
* Median Net Worth of Canadian families in 2016: $295,100
* Average annual household expenditures on goods a& services: $62,183
* Median value in principal residence: $349,000
* Highest net annual savings amount (Age 35-44): $10,120
* Number of Canadian families holding a mortgage: 38.4%
* Median Mortgage value of Principal residence: $190,000
* Debt to disposable income ratio average: 172.1
* Total value of all assets held by Canadians in 2016: 12 Trillion dollars
* The principal residence was the single largest asset held (of the 12 Trillion): 32%
* Private pensions was the 2nd largest grouping of assets at 29.2%
* The average borrowing rate for Canadian mortgages: 2.94%
* 74% were fixed rate, 21% were variable and 5% blended.
* 48% of Canadians do not save or invest at all
* 54% of Canadians do not budget regularly
* 1 in 3 Canadians have lost at least 20% in one year
* 51% of Canadians took NO ACTION after losing at least 20% in one year.
* 22% of those people either, hired or fired an advisor

Financial advice landscape:
* # of households in Canada: 13,300,000
* Households with an advisor 5,300,000
* % of households dissatisfied with existing advisor 1,100,000

Target Market(s)

Investors, ages 22-55

Industry/Entity Type

Financial

Font styles to use
Sans Serif

Colors

Designer to choose colors to be used in the design.

Requirements
Must have
• Header: Financial landscape of the average Canadian
Nice to have
• There is a lot of numbers and percentages, find a way to deliver the info using a mix of images, numbers, pictures etc.

```html
<!DOCTYPE html>
<html lang="en">
<head>
<meta charset="utf-8">
<title>How Do You Compare to the Average Canadian?</title>
<link rel="stylesheet" href="https://fonts.googleapis.com/css2?family=Lato:wght@300;400;700;900&family=Noto+Serif:ital,wght@1,400&display=swap">
<style>
  :root {
    --red: #e0453c;
    --red-dark: #c9352e;
    --red-deep: #a8281f;
    --cream: #f6f1ec;
    --navy: #3a4760;
    --navy-dark: #2f3a50;
    --teal: #6cc7b5;
    --yellow: #f3b43c;
    --gold: #d9a03a;
    --blue: #2a72c4;
    --ink: #1d1d22;
    --white: #ffffff;
    --box: #f1efec;
  }
  * { margin: 0; padding: 0; box-sizing: border-box; }
  html, body { width: 1200px; height: 2250px; overflow: hidden; background: var(--cream); }
  body { font-family: "Lato", sans-serif; position: relative; color: var(--ink); }
  .abs { position: absolute; }
  .serif-italic { font-family: "Noto Serif", serif; font-style: italic; font-weight: 400; }
  .center { text-align: center; }

  /* year tab */
  .year-tab { left: 525px; top: 0; width: 150px; height: 30px; background: var(--red); border-radius: 0 0 8px 8px; color: var(--white); font-size: 17px; font-weight: 700; line-height: 30px; text-align: center; }
  .year-tab span { font-weight: 400; opacity: .75; }

  /* hero */
  .hero { left: 21px; top: 38px; width: 1158px; height: 580px; background: var(--red); overflow: hidden; }
  .hero-band-left { left: 0; top: 0; width: 291px; height: 100%; background: var(--red-dark); }
  .hero-band-right { right: 0; top: 0; width: 287px; height: 100%; background: var(--red-dark); }
  .hero-leaf { left: 390px; top: 20px; width: 380px; height: 520px; background: radial-gradient(ellipse at center, #d23b33 0%, #d8403a 60%, rgba(224,69,60,0) 75%); }
  .hero-people { left: 256px; top: 158px; width: 640px; height: 120px; border-radius: 12px; background: linear-gradient(90deg, #f2c595, #e8b07c); opacity: .9; }
  .hero-title { left: 0; top: 276px; width: 1080px; text-align: center; color: var(--white); font-weight: 900; font-size: 66px; letter-spacing: -1px; line-height: 1; }
  .hero-rule { top: 360px; height: 0; border-top: 3px dotted rgba(255,255,255,.8); }
  .hero-to { left: 0; top: 344px; width: 1080px; text-align: center; color: var(--white); font-size: 20px; }
  .hero-sub { left: 0; top: 364px; width: 1080px; text-align: center; color: var(--white); font-weight: 300; font-size: 80px; letter-spacing: 1px; line-height: 1; }
  .hero-q { left: 940px; top: 268px; color: var(--white); font-weight: 300; font-size: 170px; line-height: 1; }

  /* snapshot */
  .snap-kicker { left: 0; top: 636px; width: 1200px; color: var(--red); font-size: 31px; }
  .snap-kicker-rule { left: 480px; top: 674px; width: 355px; border-top: 1px solid #b9b3ad; }
  .snap-title { left: 0; top: 676px; width: 1200px; font-weight: 900; font-size: 40px; letter-spacing: -.5px; }
  .icon-disc { width: 138px; height: 138px; border-radius: 50%; background: var(--blue); border: 6px solid var(--yellow); }
  .stat-kicker { color: var(--red); font-size: 26px; }
  .stat-label { font-weight: 900; font-size: 27px; letter-spacing: -.3px; }
  .red-box { background: var(--red); color: var(--white); font-weight: 900; font-size: 56px; text-align: center; line-height: 81px; height: 81px; border-radius: 6px; letter-spacing: -1px; }
  .dot-h { border-top: 3px dotted var(--red); height: 0; }
  .dot-v { border-left: 3px dotted var(--red); width: 0; }

  /* navy panel */
  .navy { left: 0; top: 1122px; width: 1200px; height: 870px; background: var(--navy); }
  .navy-split { left: 0; top: 1340px; width: 1200px; height: 8px; background: var(--navy-dark); }
  .teal-kicker { color: var(--teal); font-size: 22px; }
  .white-label { color: var(--white); font-weight: 900; font-size: 28px; letter-spacing: -.3px; }
  .white-box { background: var(--box); color: var(--navy); font-weight: 900; font-size: 62px; height: 80px; line-height: 80px; text-align: center; border-radius: 6px; letter-spacing: -1px; }
  .divider-v { border-left: 3px dotted rgba(255,255,255,.25); width: 0; }
  .yellow-big { color: var(--yellow); font-weight: 900; letter-spacing: -1px; line-height: 1; }
  .art { border-radius: 14px; }
  .scale-art { left: 180px; top: 1395px; width: 826px; height: 465px; }

  .ribbon { left: 100px; top: 1881px; width: 1018px; height: 66px; }
  .ribbon-text { left: 100px; top: 1881px; width: 1018px; height: 66px; line-height: 66px; color: var(--white); font-weight: 300; font-size: 36px; text-align: center; }
  .ribbon-text b { color: var(--yellow); font-weight: 900; font-size: 32px; }

  /* bottom */
  .bottom { left: 0; top: 1992px; width: 1200px; height: 258px; background: var(--red); overflow: hidden; }
  .assets-art { left: 83px; top: 30px; width: 420px; height: 420px; border-radius: 50%; background: var(--yellow); }
  .assets-frame { left: 38px; top: 123px; width: 510px; height: 200px; border: 2px dashed rgba(255,255,255,.5); }
  .tag { left: 385px; top: 66px; background: var(--white); color: var(--red); font-weight: 900; font-size: 21px; padding: 4px 14px; border-radius: 14px; transform: rotate(12deg); }
  .assets-l1 { left: 90px; top: 136px; width: 410px; font-weight: 900; font-size: 22px; color: var(--ink); }
  .assets-l2 { left: 90px; top: 163px; width: 410px; font-weight: 400; font-size: 32px; color: var(--ink); }
  .assets-big { left: 115px; top: 200px; font-weight: 900; font-size: 120px; color: var(--white); line-height: 1; letter-spacing: -4px; }
  .assets-unit { left: 262px; top: 202px; font-weight: 900; font-size: 54px; color: var(--white); line-height: 1; }
  .bottom-divider { left: 600px; top: 20px; height: 240px; border-left: 3px dotted rgba(255,255,255,.4); }
  .rate-art { top: 42px; height: 96px; border-radius: 12px; }
  .rate-title { left: 626px; top: 162px; color: var(--white); font-weight: 300; font-size: 58px; line-height: 1; }
  .rate-sub { left: 626px; top: 220px; color: var(--white); font-weight: 900; font-size: 34px; line-height: 1; }
  .rate-box { left: 1024px; top: 178px; width: 146px; height: 76px; background: var(--box); color: var(--red); font-weight: 900; font-size: 42px; line-height: 76px; text-align: center; border-radius: 6px; }
</style>
</head>
<body>

  <div class="abs year-tab">2016 <span>/ 2017</span></div>

  <header class="abs hero">
    <div class="abs hero-band-left"></div>
    <div class="abs hero-band-right"></div>
    <div class="abs hero-leaf" role="img" aria-label="Large maple leaf decoration"></div>
    <div class="abs hero-people" role="img" aria-label="Row of five illustrated Canadians"></div>
    <h1 class="abs hero-title">HOW DO YOU COMPARE</h1>
    <div class="abs hero-rule" style="left:156px;width:318px"></div>
    <div class="abs hero-rule" style="left:594px;width:327px"></div>
    <div class="abs hero-to serif-italic">to the</div>
    <div class="abs hero-sub">AVERAGE CANADIAN</div>
    <div class="abs hero-q">?</div>
  </header>

  <section class="snapshot">
    <div class="abs snap-kicker serif-italic center">The Average</div>
    <div class="abs snap-kicker-rule"></div>
    <h2 class="abs snap-title center">CANADIAN SNAPSHOT</h2>

    <div class="abs icon-disc" style="left:206px;top:776px" role="img" aria-label="Hand holding cash icon"></div>
    <div class="abs" style="left:505px;top:742px;width:190px;height:210px;border-radius:10px;background:linear-gradient(var(--blue) 0 38%, var(--yellow) 38% 100%)" role="img" aria-label="House with dollar bill icon, labelled In 2016"></div>
    <div class="abs icon-disc" style="left:864px;top:776px" role="img" aria-label="Money bag icon"></div>

    <div class="abs stat-kicker serif-italic center" style="left:100px;top:920px;width:350px">Average Canadian</div>
    <div class="abs stat-label center" style="left:100px;top:952px;width:350px">HOUSEHOLD INCOME</div>
    <div class="abs red-box" style="left:129px;top:1002px;width:297px">$76,900</div>

    <div class="abs stat-kicker serif-italic center" style="left:752px;top:920px;width:350px">Median Net Worth of</div>
    <div class="abs stat-label center" style="left:752px;top:952px;width:350px">CANADIAN FAMILIES</div>
    <div class="abs red-box" style="left:777px;top:1002px;width:299px">$295,100</div>

    <div class="abs dot-h" style="left:432px;top:1040px;width:340px"></div>
    <div class="abs dot-v" style="left:599px;top:978px;height:62px"></div>
  </section>

  <section class="abs navy"></section>
  <div class="abs navy-split"></div>

  <div class="abs art" style="left:82px;top:1148px;width:143px;height:150px;background:linear-gradient(135deg,#e8e4de,#d9a33a)" role="img" aria-label="House with coin illustration"></div>
  <div class="abs teal-kicker serif-italic" style="left:288px;top:1148px">Median value in</div>
  <div class="abs white-label" style="left:245px;top:1175px">PRINCIPAL RESIDENCE</div>
  <div class="abs white-box" style="left:245px;top:1218px;width:292px">$349,000</div>

  <div class="abs divider-v" style="left:600px;top:1140px;height:180px"></div>

  <div class="abs art" style="left:645px;top:1162px;width:157px;height:136px;background:var(--red)" role="img" aria-label="Piggy bank with coin illustration"></div>
  <div class="abs teal-kicker serif-italic center" style="left:790px;top:1150px;width:310px">Highest Net Annual</div>
  <div class="abs white-label center" style="left:790px;top:1177px;width:310px">SAVINGS AMOUNT</div>
  <div class="abs white-box" style="left:812px;top:1218px;width:293px">$10,120</div>
  <div class="abs" style="left:1127px;top:1242px;width:32px;height:44px;border-radius:6px;background:#e3a15b" role="img" aria-label="Small person icon"></div>
  <div class="abs serif-italic" style="left:990px;top:1308px;color:#c9cfd9;font-size:19px">Age 35-44</div>

  <svg class="abs scale-art" viewBox="0 0 826 465" role="img" aria-label="Balance scale weighing a coin against a house">
    <path d="M14 0 H812 Q826 0 826 14 V226 Q826 240 812 240 H475 V465 H351 V240 H14 Q0 240 0 226 V14 Q0 0 14 0 Z" fill="#8a6a3e" opacity=".55"/>
  </svg>

  <div class="abs teal-kicker serif-italic center" style="left:40px;top:1640px;width:460px">Number of Canadian families</div>
  <div class="abs white-label center" style="left:40px;top:1678px;width:460px;font-size:32px">HOLDING A MORTGAGE</div>
  <div class="abs yellow-big center" style="left:40px;top:1730px;width:460px;font-size:76px">38.4%</div>

  <div class="abs teal-kicker serif-italic center" style="left:700px;top:1643px;width:475px">Median Mortgage value of</div>
  <div class="abs white-label center" style="left:700px;top:1681px;width:475px;font-size:32px">PRINCIPAL RESIDENCE</div>
  <div class="abs yellow-big center" style="left:700px;top:1728px;width:475px;font-size:86px">$190,000</div>

  <svg class="abs ribbon" viewBox="0 0 1018 66" aria-hidden="true">
    <polygon points="0,8 40,8 40,58 0,58 18,33" fill="#a8281f"/>
    <polygon points="1018,8 978,8 978,58 1018,58 1000,33" fill="#a8281f"/>
    <rect x="22" y="0" width="974" height="66" fill="#e0453c"/>
  </svg>
  <div class="abs ribbon-text">DEBT TO DISPOSABLE INCOME RATIO AVERAGE &nbsp;: <b>172.1</b></div>

  <section class="abs bottom">
    <div class="abs assets-art" role="img" aria-label="Money bag illustration holding the total assets figure"></div>
    <div class="abs assets-frame"></div>
    <div class="abs tag">In 2016</div>
    <div class="abs assets-l1 center">TOTAL VALUE OF ALL ASSETS</div>
    <div class="abs assets-l2 center">HELD BY CANADIANS</div>
    <div class="abs assets-big">12</div>
    <div class="abs assets-unit">TRILLION<br>DOLLARS</div>

    <div class="abs bottom-divider"></div>

    <div class="abs rate-art" style="left:685px;width:100px;background:var(--yellow);border-radius:50%" role="img" aria-label="Clock icon"></div>
    <div class="abs rate-art" style="left:862px;width:98px;background:#e8b07c" role="img" aria-label="Illustrated Canadian figure"></div>
    <div class="abs rate-art" style="left:1035px;width:83px;background:var(--yellow)" role="img" aria-label="Money bag icon"></div>

    <div class="abs rate-title">THE AVERAGE</div>
    <div class="abs rate-sub">BORROWING RATE</div>
    <div class="abs rate-box">2.94%</div>
  </section>

</body>
</html>
```